Makeup Artist needs flyers to present his service package

I need a flyer to apply for my newly founded startup. I am an independent partner of the young brand Glamour Quest. Both my name "Marlene Kuvecht" and the attached logo should be represented, with the name in the foreground. The design should be clear and bright. The focus is on the professionalism of Marlene Kuvecht. The following topics / categories should be included in the flyer: 1.) Presentation of the person 2.) Skills Update (for the professional line) 3.) Style Update (for the private customer) 4.) Contact Text suggestions are attached as a file.

Target Market(s)

TV productions, high-priced private customers

Colors
9d9d9d
ffffff
474747

Requirements
Should not have
• No flowers, nothing playful. Not romantic.

```html
<!DOCTYPE html>
<html lang="de">
<head>
<meta charset="utf-8">
<title>Glamour Quest – Marlene Kuvecht Flyer</title>
<link href="https://fonts.googleapis.com/css2?family=Lato:wght@400;700;900&family=Raleway:wght@300;400&display=swap" rel="stylesheet">
<style>
:root{
  --grey:#9d9d9d;
  --white:#ffffff;
  --dark:#474747;
  --ink:#2e2e2e;
  --page:#f2f2f2;
}
*{margin:0;padding:0;box-sizing:border-box}
html,body{width:800px;height:1200px;overflow:hidden;background:var(--page);font-family:"Lato",sans-serif;color:var(--ink)}
.canvas{position:relative;width:800px;height:1200px}
.flyer{position:absolute;top:360px;width:370px;height:480px;background:var(--white);overflow:hidden;box-shadow:0 6px 18px rgba(0,0,0,.25)}
.flyer--front{left:20px}
.flyer--back{left:410px}

/* Front */
.portrait{position:absolute;left:0;top:0;width:370px;height:420px;background:linear-gradient(180deg,#8a8a8a 0%,#b5b5b5 45%,#d8d8d8 80%,#ffffff 100%)}
.brand{position:absolute;left:16px;top:26px;display:flex;align-items:center;gap:6px;font-family:"Lato",sans-serif;font-weight:700;font-size:11px;letter-spacing:3px;color:var(--white)}
.brand__dot{width:10px;height:10px;border-radius:50%;background:var(--white)}
.title-band{position:absolute;left:0;top:305px;width:208px;height:30px;background:var(--dark);color:var(--white);font-weight:900;font-size:23px;letter-spacing:.5px;padding-left:16px;line-height:30px}
.name-box{position:absolute;left:0;top:335px;width:208px;height:68px;background:var(--white);padding:4px 0 0 16px;font-family:"Raleway",sans-serif;font-weight:300;font-size:30px;line-height:30px;color:var(--dark);letter-spacing:.5px}
.services{position:absolute;left:16px;top:412px;width:340px;font-size:6.6px;font-weight:700;text-transform:uppercase;line-height:8.5px;color:var(--dark)}
.web{position:absolute;left:16px;top:454px;display:flex;align-items:center;gap:6px;font-size:8.5px;font-weight:700;color:var(--ink)}
.web__rule{width:100px;height:1px;background:var(--dark)}

/* Back */
.hero{position:absolute;left:0;top:0;width:370px;height:136px;background:linear-gradient(90deg,#8c7466 0%,#a08878 45%,#6b6b6b 60%,#3a3a3a 100%)}
.tab{position:absolute;height:13px;background:var(--grey);color:var(--white);font-size:7px;font-weight:700;line-height:13px;padding-left:10px}
.tab--me{left:4px;top:146px;width:60px}
.tab--skills{left:4px;top:222px;width:172px}
.tab--style{left:190px;top:222px;width:172px}
.me-photo{position:absolute;left:16px;top:163px;width:48px;height:42px;background:linear-gradient(135deg,#555,#999)}
.text{position:absolute;font-size:5px;line-height:6.2px;color:var(--dark);text-align:justify}
.me-text{left:80px;top:146px;width:280px}
.col{position:absolute;top:240px;width:160px;font-size:5px;line-height:6.2px;color:var(--dark)}
.col--skills{left:14px}
.col--style{left:196px;text-align:justify}
.col h3{font-size:6.4px;font-weight:700;margin-bottom:6px;color:var(--ink)}
.col p{margin-bottom:5px}
.bullets{list-style:none;margin:4px 0 7px}
.bullets li{position:relative;padding-left:9px;margin-bottom:3px}
.bullets li::before{content:"";position:absolute;left:0;top:1px;width:4px;height:4px;border-radius:50%;border:1px solid var(--dark)}
.contact{position:absolute;left:0;top:440px;width:185px;height:40px;background:var(--dark);color:var(--white);padding:6px 0 0 14px;font-size:5.4px;line-height:7px}
.contact__row{display:flex;gap:10px;align-items:center}
.contact__item{display:flex;align-items:center;gap:2px}
</style>
</head>
<body>
<div class="canvas">

  <section class="flyer flyer--front">
    <div class="portrait" role="img" aria-label="Black and white portrait of the makeup artist with short hair and dark glasses"></div>
    <div class="brand"><span class="brand__dot"></span>GLAMOUR QUEST</div>
    <div class="title-band">MAKEUP-BY</div>
    <div class="name-box">MARLENE<br>KUVECHT</div>
    <p class="services">Make-up &amp; Hairstyling in München, für TV, Foto, Event Veranstaltung, Business Make-up, Weiterbildung, Brautstyling, Make-up Coaching &amp; Workshops</p>
    <div class="web">www.glamour-quest.de/muenchen <span class="web__rule"></span></div>
  </section>

  <section class="flyer flyer--back">
    <div class="hero" role="img" aria-label="Makeup palette and brushes on a dressing table"></div>

    <div class="tab tab--me">ME</div>
    <div class="me-photo" role="img" aria-label="Small photo of the artist at work"></div>
    <p class="text me-text">Seit vielen Jahren arbeite ich mit großer Leidenschaft für bekannte TV-, Foto- und Showformate als Makeup Artist und Hairstylistin. Katrin Bergmann und Frieda Lorenz habe ich für Projekte im In- und Ausland begleitet, um mit ihnen an traumhaften Plätzen zu drehen. Bei verschiedenen Produktionen habe ich auch mit nationalen und internationalen Schauspielern sowie mit prominenten Politikern gearbeitet. Moderatoren und Celebrities vertrauen meiner fachlichen Kompetenz und schätzen meine Integrität. Nun habe ich mir auch noch einen Traum mit meinem Atelier in München erfüllt. Hier kann ich nun endlich jeden Beauty-Interessierten, ob Frau oder Mann, mit meinem Wissen und meiner Dienstleistung zur Seite stehen. Ob für ein Event oder eine Businessveranstaltung, den Roten Teppich oder den Brautstyling am schönsten Tag des Lebens.</p>

    <div class="tab tab--skills">SKILLS UPDATE</div>
    <div class="tab tab--style">STYLE UPDATE</div>

    <div class="col col--skills">
      <h3>Das ist meine professionelle Linie für:</h3>
      <ul class="bullets">
        <li>HDTV Produktionen</li>
        <li>Fotoshootings und Produktionen in der Greenbox</li>
        <li>Fernsehsender, Fotografen und Agenturen</li>
        <li>Events, Show- und Galaveranstaltungen</li>
        <li>Auftritte auf dem Roten Teppich</li>
      </ul>
      <p>Um den Anforderungen von HD und 4K gerecht werden zu können, arbeite ich ausschließlich mit professionellen Ultra-HD Makeup Produkten. Bei Fotoshootings und Events verwende ich ebenfalls nur qualitativ hochwertige Markenprodukte, um den höchsten Ansprüchen gerecht werden zu können und eine perfekte Leistung zu garantieren. Außerdem gebe ich mein Wissen weiter an Fachkundige aus dem Kosmetik- oder Friseurhandwerk.</p>
      <h3>In speziellen Workshops für Profis werden:</h3>
      <ul class="bullets">
        <li>Die Techniken des HDTV Makeups</li>
        <li>Produktlehre</li>
        <li>Makeup für Greenbox</li>
        <li>Hairstyling</li>
        <li>Braut Makeup und Brautstyling</li>
      </ul>
    </div>

    <div class="col col--style">
      <h3>Mein schönes Ich</h3>
      <p>Sie sind Unternehmerin oder Businessfrau, Sie stellen Projekte vor und haben Videokonferenzen. Mit Ihrer Kompetenz stehen Sie im Fokus. Haben Sie ein Bewerbungsgespräch auf das Sie fachlich perfekt vorbereitet sind, aber noch keinen Gedanken über Ihr Styling gemacht haben?</p>
      <p>Unterstreichen Sie Ihren Auftritt mit einem strahlenden, frischen und femininen Makeup. Ein Business Makeup soll unaufdringlich aber selbstbewusst den eigenen Typ in Szene setzen. Ein gepflegter Look, der Ihrer Kompetenz noch das „i Tüpfelchen“ aufsetzt.</p>
      <p>Sie sind eingeladen und Sie wollen ganz besonders schön aussehen. Ich unterstütze Sie.</p>
      <p>Im individuellen Einzelcoaching oder auch in einem Makeup Workshop lernen Sie die geheimen Tricks und Produkte eines professionellen Makeup Artist kennen. Sehen Sie wie schön Sie wirklich sind. Bald werden Sie Ihr eigener Beauty Profi sein, für Privat und Business.</p>
      <p>Alle Workshops können auch von Unternehmen als Corporate Makeup oder Firmenevent gebucht werden. Wenn nicht in München dann woanders, auch das ist möglich.</p>
      <p>Ich freue mich auf Sie<br>Ihre Marlene Kuvecht</p>
    </div>

    <div class="contact">
      <div>SPRECHEN SIE MICH DIREKT AN, UNTER</div>
      <div>marlene.kuvecht@glamour-quest.de</div>
      <div class="contact__row">
        <span class="contact__item">
          <svg width="6" height="6" viewBox="0 0 10 10" aria-hidden="true"><circle cx="5" cy="5" r="5" fill="#fff"/><path d="M3 2.5l1.2 1.3-.6.8c.5.9 1 1.4 1.8 1.8l.8-.6 1.3 1.2-.8.9C4.8 7.6 2.4 5.2 2.1 3.3z" fill="#474747"/></svg>
          089/5550123</span>
        <span class="contact__item">
          <svg width="6" height="6" viewBox="0 0 10 10" aria-hidden="true"><circle cx="5" cy="5" r="5" fill="#fff"/><rect x="3.5" y="2" width="3" height="6" rx=".6" fill="#474747"/></svg>
          0151/5550199</span>
      </div>
    </div>
  </section>

</div>
</body>
</html>
```